Brochure Design Project

Our company is KMV Sable Ridge. (no LOGO)

We are a restaurant marketing and advertising service. We market restaurants menus by producing a menu guide, distributing flyers and post cards, and also placing the restaurants menu on our website for delivery.

We make restaurants more profitable, by making their food more accessible. Marketing restaurants on search engines, websites, plazanet, wunq, zintro, and a total of 21 different marketing techniques that make restaurants more money.

Key Point: This is all done at NO COST to the restaurant.

We are looking for a design for a brochure that will be mailed as well as handed to restaurateurs.

In my attached file I am including our sales letter. The letter can stay in letter form for the inside of a tri-fold brochure or it can be part of your design.

For more information about our service, please read the attached sales letter.
Updates

Target Market(s)

Restaurant Owners and General managers

Industry/Entity Type

Advertising

Requirements
Must have
• Must look attractive and Eye-catching

```html
<!DOCTYPE html>
<html lang="en">
<head>
<meta charset="utf-8">
<title>KMV Sable Ridge – Tri-Fold Brochure Inside</title>
<link href="https://fonts.googleapis.com/css2?family=Lexend+Deca:wght@600&family=Varela+Round&family=Arimo:wght@400;700&family=Arvo:wght@700&display=swap" rel="stylesheet">
<style>
:root{
  --page-bg:#22406a;
  --teal:#5cc2ce;
  --sand:#cdbfa3;
  --panel-grey:#d6d2cb;
  --paper:#ffffff;
  --ink:#111111;
  --muted:#555555;
  --poll-dark:#1c1c1c;
}
*{box-sizing:border-box;margin:0;padding:0}
html,body{width:1200px;height:1028px;overflow:hidden}
body{background:var(--page-bg);position:relative;font-family:"Arimo",Arial,sans-serif;color:var(--ink)}
.brochure{position:absolute;left:30px;top:69px;width:1140px;height:890px;background:var(--paper);box-shadow:0 10px 40px rgba(0,0,0,.45)}
.panel{position:absolute;top:0;height:890px;overflow:hidden}

/* left panel */
.panel-intro{left:0;width:386px;background:var(--paper)}
.band{position:absolute;left:0;width:100%;height:37px;background:var(--sand)}
.band-top{top:0}
.band-bottom{bottom:0;background:var(--panel-grey)}
.portrait{position:absolute;left:172px;top:30px;width:115px;height:340px;background:linear-gradient(180deg,#d9c7b8 0%,#a89185 55%,#8a7468 100%);border-radius:40px 40px 6px 6px}
.accent-rule{position:absolute;left:42px;top:369px;width:344px;height:9px;background:var(--teal)}
.headline{position:absolute;left:48px;top:412px;width:320px;font-family:"Lexend Deca",sans-serif;font-weight:600;font-size:35px;line-height:42px;letter-spacing:-.5px}
.tagline{position:absolute;left:48px;top:696px;width:300px;font-weight:700;font-size:19px;line-height:22px;letter-spacing:-.3px}

/* middle panel */
.panel-letter{left:386px;width:370px;background:var(--teal)}
.vertical-domain{position:absolute;left:-262px;top:490px;width:580px;transform:rotate(-90deg);font-family:"Varela Round",sans-serif;font-size:54px;letter-spacing:1px;color:transparent;-webkit-text-stroke:2px #ffffff;text-align:center;white-space:nowrap}
.letter{position:absolute;left:66px;top:32px;width:294px;font-size:11.4px;line-height:17.4px;color:#10262a}
.letter p{margin-bottom:17.4px}
.letter .subhead{font-weight:700;margin-bottom:17.4px}

/* right panel */
.panel-contact{left:756px;width:384px;background:var(--panel-grey)}
.cta{position:absolute;left:40px;top:88px;width:330px;font-weight:700;font-size:27.5px;line-height:35px;letter-spacing:-.4px}
.poll{position:absolute;left:40px;top:292px;width:302px;height:326px;border:4px solid #fff;border-radius:12px;background:linear-gradient(180deg,#f4f4f4,#c8c8c8);box-shadow:0 4px 10px rgba(0,0,0,.35)}
.poll-question{margin:14px 12px 0;height:52px;background:linear-gradient(180deg,#3a3a3a,var(--poll-dark));border-radius:4px;color:#fff;font-weight:700;font-size:12.5px;line-height:17px;padding:10px 12px}
.poll-options{list-style:none;margin:22px 0 0 14px}
.poll-options li{display:flex;align-items:center;font-size:11.5px;color:#222;height:33px}
.poll-options li::before{content:"";width:11px;height:11px;border:1px solid #888;border-radius:50%;background:#fff;margin-right:12px}
.poll-vote{margin:16px 0 0 14px;width:70px;height:26px;border-radius:6px;background:linear-gradient(180deg,#9a9a9a,#6d6d6d);color:#fff;font-weight:700;font-size:13px;display:flex;align-items:center;justify-content:center}
.poll-footer{position:absolute;left:14px;right:14px;bottom:12px;height:24px;border-radius:6px;background:#e9e9e9;border:1px solid #bbb;font-size:10.5px;color:#333;display:flex;justify-content:center;gap:26px;align-items:center}
.contact-box{position:absolute;left:20px;top:695px;width:347px;height:162px;background:var(--teal);text-align:center;padding-top:16px}
.contact-lead{font-size:20px}
.contact-name,.contact-phone,.contact-web{font-family:"Arvo",serif;font-weight:700;font-size:22px;line-height:26px}
.contact-web{margin-top:16px;font-size:23px}
</style>
</head>
<body>
<main class="brochure">
  <section class="panel panel-intro">
    <div class="band band-top"></div>
    <div class="portrait" role="img" aria-label="Photo of a smiling businesswoman in a taupe trouser suit standing full length"></div>
    <div class="accent-rule"></div>
    <h1 class="headline">We make Restaurants more profitable, by Making their food more accessible!</h1>
    <p class="tagline">Restaurant Marketing and Advertising<br>specializing in Delivery</p>
    <div class="band band-bottom"></div>
  </section>

  <section class="panel panel-letter">
    <div class="vertical-domain">kmvsableridge.com</div>
    <div class="letter">
      <p>KMV Sable Ridge is a restaurant marketing and advertising service that specializes in delivery. We deliver food from a variety of restaurants to people at their homes, offices or hotel rooms.</p>
      <p>Customers can order food directly online, at our website, or by calling our office. Once we receive an order, we'll place it at your restaurant by phone or fax. Our mobile waiter will be dispatched to your restaurant and wait wherever the restaurant designate, and when the food's ready, he or she will place the order in a thermal bag to keep it hot and deliver it to the customer. We handle all the collections and pay you every week for the orders we delivered the previous week.</p>
      <p>We agree with Northgate Card Co. who, in their Restaurant Merchants Briefing Newsletter, has recommended that restauranteurs form an alliance with a delivery service to capitalize on the trend in today's busy two wage-earner economy in which people just want some food delivered - other than just pizza! Many individuals or groups don't have time to come in to your restaurant to enjoy the food there or pick it up themselves. They just want to get something delivered. We divert many of those customers to your restaurant sales!</p>
      <p>We handle all the marketing, order-taking and delivery (and all that those things entail). We'll expand your customer base and increase your bottom line. And it doesn't cost you anything to participate!</p>
      <p class="subhead">Reach More Potential Customers!</p>
      <p>Your customers are searching your business and making their decisions online more than ever. KMV Sable Ridge helps you reach thousands of potential customers on search engines and social media platforms. We manage online advertising so you don't miss out on any additional business.</p>
    </div>
  </section>

  <section class="panel panel-contact">
    <h2 class="cta">For more information on forming an alliance with us please schedule an initial consultation.</h2>
    <div class="poll">
      <div class="poll-question">How much do you spend a month on Marketing?</div>
      <ul class="poll-options">
        <li>$0-$200</li>
        <li>$200-$350</li>
        <li>$350-$500</li>
        <li>&gt;$500</li>
      </ul>
      <div class="poll-vote">Vote</div>
      <div class="poll-footer"><span>View Results</span><span>Pollbox.net</span></div>
    </div>
    <div class="contact-box">
      <p class="contact-lead">Please talk to us :</p>
      <p class="contact-name">Rob Calder</p>
      <p class="contact-phone">555-014-2290 (cell)</p>
      <p class="contact-web">kmvsableridge.com</p>
    </div>
  </section>
</main>
</body>
</html>
```